New CD - "Tunes About Marla" (Jazz piano standards)

We need a CD design for album of jazz piano standards. The music is elegant, fun, and artistic. Appeals to all lovers of Halvorsen, Brenton, Dubrow, etc. Includes Red Harbor, Can't Stop Dancin', Harbor Serenade, She Keeps A Secret In Her Pocket, Rain Falls On Quiet Streets, Lazy Tuesday, (Tonight) Across The Meadow, Hours by Candle and Lace, When Rivers Bend, Only If You Call, Your Quiet Spark, She Always Left The Door, Remarkable Dawn, Prelude Op. 28, No. 15 "Lamplight"/T. Varga.

Target Market(s)

Anyone who likes piano music.

```html
<!DOCTYPE html>
<html lang="en">
<head>
<meta charset="utf-8">
<title>Tunes About Marla — Album Cover</title>
<link rel="stylesheet" href="https://fonts.googleapis.com/css2?family=Roboto+Slab:wght@200;300&display=swap">
<style>
  :root {
    --backdrop: #a3a7a5;
    --sky-dark: #2f3a33;
    --sky-mid: #5d6a5c;
    --haze: #b7bba6;
    --horizon-warm: #c9a58f;
    --city: #4f5f5c;
    --water: #2a3b3a;
    --water-deep: #1c2626;
    --title-white: #f4f2ec;
    --title-gold: #f0a91e;
  }
  * { box-sizing: border-box; margin: 0; padding: 0; }
  html, body {
    width: 1200px;
    height: 900px;
    overflow: hidden;
    background: var(--backdrop);
  }
  .album-cover {
    position: absolute;
    left: 190px;
    top: 40px;
    width: 820px;
    height: 820px;
    overflow: hidden;
    box-shadow: 0 6px 18px rgba(0, 0, 0, 0.25);
  }
  .cover-artwork {
    position: absolute;
    inset: 0;
    background:
      radial-gradient(ellipse 55% 40% at 40% 42%, rgba(206, 210, 190, 0.55), transparent 70%),
      radial-gradient(ellipse 60% 10% at 75% 68%, rgba(201, 165, 143, 0.6), transparent 75%),
      linear-gradient(to bottom,
        var(--sky-dark) 0%,
        var(--sky-mid) 30%,
        var(--haze) 55%,
        var(--horizon-warm) 66%,
        var(--city) 72%,
        var(--water) 82%,
        var(--water-deep) 100%);
  }
  .album-title {
    position: absolute;
    left: 435px;
    top: 185px;
    font-family: "Roboto Slab", serif;
    font-weight: 300;
    line-height: 1;
  }
  .album-title .title-lead {
    display: block;
    font-size: 56px;
    color: var(--title-white);
    letter-spacing: 0.5px;
  }
  .album-title .title-name {
    display: block;
    font-size: 124px;
    font-weight: 200;
    color: var(--title-gold);
    margin-top: -14px;
    letter-spacing: 1px;
  }
  .artist-name {
    position: absolute;
    left: 0;
    right: 0;
    top: 707px;
    text-align: center;
    font-family: "Roboto Slab", serif;
    font-weight: 300;
    font-size: 23px;
    letter-spacing: 0.85em;
    color: var(--title-white);
  }
</style>
</head>
<body>
  <main class="album-cover">
    <div class="cover-artwork" role="img" aria-label="Misty painted scene: a young woman holding a glass bottle releasing smoke shaped like music notes, above a hazy city skyline across dark water under a cloudy grey-green sky"></div>
    <h1 class="album-title">
      <span class="title-lead">Tunes About</span>
      <span class="title-name">Marla</span>
    </h1>
    <p class="artist-name">Everett Lindqvist</p>
  </main>
</body>
</html>
```